Email to encourage School District Employees to save for retirement using the 457 Retirement

This is an email to encourage School District Employees to save for retirement using the 457 Retirement Plan. Highlights of the plan include no 10% TBO penalty for taking money before age 59 1/2 another highlight is that they can save money on taxes by using the plan to reduce their taxable income. This is why they should use the this plan first, not a 403(b). We are financial advisers helping school employees

Target Market(s)

School Employees, Teachers, Administrators, Secretaries. Planning for retirement and reduce taxes.

Industry/Entity Type

Financial Planning

Colors

Designer to choose colors to be used in the design.

Requirements
Must have
• [TEXT]:
• 457 PLAN FIRST
• Are you contributing to a 403(b) retirement account? Here’s why you should consider a 457 plan first
• •No TBO 10% Penalty
• If you leave your job, you can take distributions at any time, no matter your age without penalty, unlike 403(b) accounts which impose a 10% penalty if under age 59 ½.
• •More Tax-Deferral
• You can contribute to both a 457 and 403(b) plan simultaneously. This means defer and save up to $37,000 annually or $49,000 if age 50+. This is especially appealing to employees who have substantially high income and are trying to reduce taxable income.
• DON’T COMPLETELY RELY ON THAT PENSION TO PROVIDE FOR YOUR RETIREMENT. TAKE YOUR FINANCIAL FUTURE INTO YOUR OWN HANDS WITH A 457
• LEARN MORE CALL TODAY
• 800-513-7692
• [8pt font]:
• Securities offered through Bellwether Pine Brokerage, L.P. Member - NASTO/DRUV | 4876 Orchard Row K, Ste 510, Lancaster, CA 90817 | 800.513.7692 | CA Ins. Lic. #0K47318, #0519634, #0K38205, #0761248
Nice to have
• We would like to see a design that shows a teacher writing on chalkboard "Why you should use a 457 Plan first"
• Please emphasize that there is no 10% penalty and that they can save more and reduce taxes using 457 plan. Please use images and themes related to School/Education, money, and retirement.

```html
<!DOCTYPE html>
<html lang="en">
<head>
<meta charset="utf-8">
<title>District Approved 457 Retirement Plan</title>
<link href="https://fonts.googleapis.com/css2?family=PT+Sans:wght@400;700&family=Gochi+Hand&display=swap" rel="stylesheet">
<style>
  :root {
    --brand-blue: #1a6fb9;
    --heading-blue: #1566c0;
    --page-grey: #eeeef0;
    --band-grey: #f4f4f5;
    --footer-grey: #f3f3f3;
    --text-dark: #3a3d42;
    --text-body: #5f6368;
    --text-muted: #9a9a9a;
    --rule: #d8d8dc;
    --white: #ffffff;
    --chalk: #eef0f2;
    --board-dark: #1f2329;
    --board-mid: #3b4049;
    --shirt-light: #dfe8f5;
    --shirt-mid: #b9cae2;
  }
  * { margin: 0; padding: 0; box-sizing: border-box; }
  html, body { width: 735px; height: 1200px; overflow: hidden; background: var(--white); }
  body { font-family: "PT Sans", Arial, sans-serif; color: var(--text-body); }
  .email { width: 735px; height: 1200px; display: flex; flex-direction: column; }

  .masthead { height: 73px; flex: none; background: var(--page-grey); display: flex; align-items: center; padding-left: 20px; }
  .masthead-title { color: var(--heading-blue); font-weight: 700; font-size: 20.5px; letter-spacing: 0.1px; }

  .hero { position: relative; height: 355px; flex: none; overflow: hidden;
    background: linear-gradient(100deg, var(--board-dark) 0%, var(--board-mid) 50%, #262a31 100%); }
  .hero-portrait { position: absolute; left: 512px; top: 70px; width: 223px; height: 285px;
    background: linear-gradient(160deg, #2b3038 0%, var(--shirt-mid) 45%, var(--shirt-light) 100%);
    border-radius: 90px 0 0 0; }
  .chalk { position: absolute; left: 73px; font-family: "Gochi Hand", "Comic Sans MS", cursive; color: var(--chalk); white-space: nowrap; line-height: 1; }
  .chalk-first { top: 84px; font-size: 39px; letter-spacing: 0.5px; }
  .chalk-first u { text-decoration-thickness: 2px; text-underline-offset: 5px; }
  .chalk-second { top: 136px; font-size: 31px; letter-spacing: 0.4px; }
  .chalk-why { top: 218px; font-size: 68px; letter-spacing: 1px; }

  .benefits { height: 438px; flex: none; background: var(--page-grey); padding: 40px 0 0 97px; }
  .benefit { width: 548px; margin-bottom: 36px; }
  .benefit-title { width: 538px; font-size: 15.5px; font-weight: 700; color: var(--text-dark); padding-bottom: 6px; border-bottom: 2px solid var(--rule); margin-bottom: 8px; }
  .benefit-text { font-size: 12.3px; line-height: 22px; color: var(--text-body); }
  .benefit-text.indent { padding-left: 2px; }

  .specialist { height: 86px; flex: none; background: var(--band-grey); display: flex; align-items: center; justify-content: center; text-align: center; }
  .specialist-text { color: var(--heading-blue); font-size: 19px; line-height: 29px; }

  .cta { height: 84px; flex: none; background: var(--brand-blue); color: var(--white); text-align: center; padding-top: 16px; }
  .cta-title { font-weight: 700; font-size: 18.5px; line-height: 24px; }
  .cta-contacts { font-size: 18.5px; line-height: 30px; }

  .legal { height: 100px; flex: none; background: var(--white); text-align: center; font-size: 11.8px; line-height: 22px; color: var(--text-body); padding-top: 24px; }

  .footer { flex: 1; background: var(--footer-grey); display: flex; align-items: center; justify-content: space-between; padding: 0 48px 0 53px; font-size: 11.5px; }
  .footer-copy { color: var(--text-dark); }
  .footer-copy span { color: var(--text-muted); }
  .social { display: flex; gap: 12px; color: var(--text-muted); font-size: 11px; }
</style>
</head>
<body>
<div class="email">
  <header class="masthead">
    <h1 class="masthead-title">DISTRICT APPROVED 457 RETIREMENT PLAN</h1>
  </header>

  <section class="hero">
    <div class="hero-portrait" role="img" aria-label="Photo of a smiling teacher in a light blue shirt writing on the chalkboard"></div>
    <p class="chalk chalk-first">457 Retirement Plan <u>FIRST</u></p>
    <p class="chalk chalk-second">403(b) Retirement Plan SECOND</p>
    <p class="chalk chalk-why">WHY?</p>
  </section>

  <section class="benefits">
    <div class="benefit">
      <h2 class="benefit-title">NO TBO 10% PENALTY</h2>
      <p class="benefit-text indent">If you leave your job, you can take distributions at any time, no matter your age without penalty, unlike 403(b) accounts which impose a 10% penalty if under age 59 ½.</p>
    </div>
    <div class="benefit">
      <h2 class="benefit-title">MORE TAX-DEFERRAL</h2>
      <p class="benefit-text">You can contribute to both a 457 and 403(b) plan simultaneously. This means defer and save up to $37,000 annually or $49,000 if age 50+. This means you can defer and save up to this is especially appealing to employees who have substantially high income and are trying to reduce taxable income.</p>
    </div>
    <div class="benefit">
      <h2 class="benefit-title">YOUR PENSION IS NOT ENOUGH</h2>
      <p class="benefit-text indent">In most cases, the pension will only cover about 50% of your final salary. Can you afford a 50% pay cut in retirement? This is why you should establish a 457 Plan to help supplement your pension benefits.</p>
    </div>
  </section>

  <section class="specialist">
    <p class="specialist-text">SPEAK WITH A CIVIC EDUCATORS GUILD (CEG)<br>RETIREMENT SPECIALIST TODAY</p>
  </section>

  <section class="cta">
    <p class="cta-title">LEARN MORE CALL TODAY</p>
    <p class="cta-contacts">800-513-7692 • mlarkin@pinemail.net • www.marenlarkinfinancial.com</p>
  </section>

  <section class="legal">
    <p>Securities offered through Bellwether Pine Brokerage, L.P. Member - NASTO/DRUV<br>
    4876 Orchard Row K, Ste 510, Lancaster, CA 90817 | 800.513.7692 | CA Ins. Lic. #0K47318, #0519634,<br>
    #0K38205, #0761248</p>
  </section>

  <footer class="footer">
    <p class="footer-copy">457 insurance © <span>copyright 2018 - Unsubscribe here</span></p>
    <div class="social">
      <span>Circlet</span><span>Folio</span><span>Chirp</span>
    </div>
  </footer>
</div>
</body>
</html>
```